Need to create a website for a luxury custom home builder in Phoenix USA. Looking forward for some creative designs including a full page video intro on homepage and should show up pretty luxurious.

```html
<!DOCTYPE html>
<html lang="en">
<head>
<meta charset="utf-8">
<title>Trueline Homes — Luxury Custom Home Builder</title>
<link href="https://fonts.googleapis.com/css2?family=Syncopate:wght@400;700&family=Montserrat:wght@400;500;600;700&display=swap" rel="stylesheet">
<style>
:root{
  --blue:#1b8fd6;
  --blue-dark:#1670bd;
  --blue-deep:#135fa3;
  --green:#12ab8a;
  --green-dark:#0e9478;
  --ink:#1d2b3a;
  --text:#4a5560;
  --muted:#eef0f3;
  --white:#ffffff;
  --frame:#a9cfe8;
}
*{margin:0;padding:0;box-sizing:border-box}
html,body{width:1200px;height:4342px;overflow:hidden}
body{position:relative;background:var(--white);font-family:"Montserrat",Arial,sans-serif;color:var(--text)}
.abs{position:absolute}
.display{font-family:"Syncopate","Arial Black",sans-serif;font-weight:700;text-transform:uppercase;letter-spacing:2px}
.btn{position:absolute;display:flex;align-items:center;justify-content:center;font-size:11px;font-weight:700;letter-spacing:1px;text-transform:uppercase;border:2px solid}
.photo{position:absolute}

/* header */
.site-header{position:absolute;top:0;left:0;width:1200px;height:70px;background:var(--white)}
.brand{position:absolute;display:flex;align-items:center;gap:8px;font-weight:700;color:var(--blue);text-transform:uppercase}
.brand .dot{width:14px;height:14px;border-radius:50%;background:var(--blue)}
.header-brand{left:108px;top:20px;font-size:21px;letter-spacing:.5px}
.main-nav{position:absolute;left:366px;top:28px;display:flex;font-size:11px;font-weight:600;color:var(--blue);text-transform:uppercase}
.main-nav span{padding:0 17px;border-right:1px solid #9fc7e3;line-height:13px}
.main-nav span:first-child{padding-left:0}
.main-nav span:last-child{border:none}
.phone-box{position:absolute;left:1001px;top:0;width:199px;height:70px;background:var(--green);color:var(--white);display:flex;align-items:center;justify-content:center;gap:8px;font-size:13px;font-weight:700;letter-spacing:.5px}

/* hero */
.hero{position:absolute;top:70px;left:0;width:1200px;height:611px;overflow:hidden;background:linear-gradient(180deg,#2d8fd0 0%,#6eb3df 35%,#9aa3ac 60%,#5b8a3c 85%,#4a7a30 100%)}
.hero .photo{inset:0}
.hero-shade{position:absolute;inset:0;background:linear-gradient(90deg,rgba(16,90,160,.55),rgba(16,90,160,0) 55%)}
.hero-kicker{left:115px;top:172px;font-size:14px;font-weight:700;letter-spacing:4px;color:var(--white)}
.hero-title{left:115px;top:198px;font-size:32px;line-height:36px;color:var(--white)}
.hero-btn{left:115px;top:328px;width:162px;height:39px;color:var(--white);border-color:var(--white);border-width:1.5px}
.hero-arrow{position:absolute;top:258px}

/* about */
.about{position:absolute;top:681px;left:0;width:1200px;height:554px;overflow:hidden;background:var(--white)}
.about-title{left:637px;top:163px;font-size:21px;line-height:29px;color:var(--blue)}
.rule{position:absolute;height:3px;background:var(--green)}
.about p{position:absolute;left:637px;top:240px;width:380px;font-size:12.5px;line-height:22px}
.about-btn{left:637px;top:369px;width:144px;height:39px;color:var(--green);border-color:var(--green)}

/* featured */
.featured{position:absolute;top:1235px;left:0;width:1200px;height:548px;background:var(--muted)}
.section-title{position:absolute;left:0;width:1200px;text-align:center;font-size:22px}
.featured .section-title{top:68px;color:var(--blue)}
.card-img{position:absolute;top:138px;width:310px;height:253px}
.card-text{position:absolute;padding:22px 30px;font-size:10px;line-height:15px;box-shadow:0 6px 18px rgba(0,0,0,.08)}
.card-text h3{font-size:13px;font-weight:700;margin-bottom:6px;text-transform:uppercase}
.card-light{background:var(--white);color:#66707a}
.card-light h3{color:var(--blue-deep)}
.card-blue{background:var(--blue);color:#dcefff}
.card-blue h3{color:var(--white)}

/* services */
.services{position:absolute;top:1783px;left:0;width:1200px;height:564px;overflow:hidden;background:linear-gradient(135deg,#1a7ccc 0%,#1b86d2 45%,#1566b0 100%)}
.services .photo{inset:0;background:linear-gradient(90deg,rgba(255,255,255,.05),rgba(255,255,255,.12) 50%,rgba(0,0,0,.06))}
.services-kicker{position:absolute;top:48px;width:1200px;text-align:center;color:var(--white);font-size:12px;letter-spacing:1px}
.services .section-title{top:68px;color:var(--white)}
.service{position:absolute;width:200px;text-align:center}
.service h3{font-family:"Syncopate","Arial Black",sans-serif;font-size:13px;font-weight:700;letter-spacing:1.5px;line-height:16px;text-transform:uppercase;margin:8px 0 8px}
.service p{font-size:9.5px;line-height:15px}
.service-light{color:#444}
.service-light h3{color:var(--ink)}
.service-green{color:#e6fff8}
.service-green h3{color:var(--white)}

/* why choose */
.why{position:absolute;top:2347px;left:0;width:1200px;height:622px;overflow:hidden;background:var(--white)}
.why-title{left:647px;top:166px;font-size:21px;line-height:29px;color:var(--white)}
.why p{position:absolute;left:647px;top:248px;width:380px;font-size:12.5px;line-height:22px;color:#e9fbf6}
.why-btn{left:641px;top:369px;width:144px;height:39px;color:var(--white);border-color:var(--white)}

/* how we build */
.how{position:absolute;top:2969px;left:0;width:1200px;height:546px;overflow:hidden;background:linear-gradient(180deg,#1b86d2,#1673c0)}
.how-title{left:115px;top:125px;font-size:24px;line-height:31px;color:var(--white)}
.how p{position:absolute;left:121px;top:204px;width:400px;font-size:12.5px;line-height:23px;color:#e3f1fc}
.how-btn{left:121px;top:342px;width:154px;height:42px;color:var(--white);border-color:var(--white)}

/* start */
.start{position:absolute;top:3515px;left:0;width:1200px;height:633px;background:var(--white)}
.start-frame{position:absolute;left:440px;top:93px;width:628px;height:449px;border:3px solid var(--frame)}
.start-accent{position:absolute;left:96px;top:116px;width:169px;height:207px;background:var(--green)}
.start-img{left:115px;top:136px;width:465px;height:351px}
.start-title{left:637px;top:209px;font-size:21px;line-height:29px;color:var(--blue)}
.start p{position:absolute;left:637px;top:294px;width:370px;font-size:12.5px;line-height:22px}
.start-btn{left:642px;top:379px;width:227px;height:44px;color:var(--blue-deep);border-color:var(--blue);font-size:10.5px}

/* footer */
.site-footer{position:absolute;top:4148px;left:0;width:1200px;height:194px;background:var(--green);color:var(--white)}
.footer-brand{position:absolute;left:0;top:94px;width:345px;text-align:center;font-size:26px;font-weight:700;letter-spacing:1px;text-transform:uppercase}
.footer-mark{position:absolute;left:157px;top:34px;width:26px;height:26px;border-radius:50%;background:var(--white)}
.footer-divider{position:absolute;left:345px;top:0;width:1px;height:194px;background:rgba(255,255,255,.45)}
.footer-rule{position:absolute;left:345px;top:107px;width:855px;height:1px;background:rgba(255,255,255,.45)}
.footer-nav{position:absolute;top:52px;font-size:11.5px;font-weight:700;text-transform:uppercase}
.copyright{position:absolute;left:379px;top:131px;font-size:11px}
.social{position:absolute;top:124px;width:28px;height:28px;border:1.5px solid var(--white);border-radius:50%}
</style>
</head>
<body>

<header class="site-header">
  <div class="brand header-brand"><span class="dot"></span>Trueline Homes</div>
  <nav class="main-nav"><span>About Us</span><span>Services</span><span>Projects</span><span>Why Us</span><span>Blogs</span><span>Contact Us</span></nav>
  <div class="phone-box">
    <svg width="13" height="13" viewBox="0 0 24 24"><path fill="#fff" d="M6.6 10.8a15.1 15.1 0 0 0 6.6 6.6l2.2-2.2c.3-.3.7-.4 1-.2 1.1.4 2.3.6 3.6.6.6 0 1 .4 1 1V20c0 .6-.4 1-1 1C10.6 21 3 13.4 3 4c0-.6.4-1 1-1h3.5c.6 0 1 .4 1 1 0 1.3.2 2.5.6 3.6.1.3 0 .7-.2 1z"/></svg>
    (555) 014 2290
  </div>
</header>

<section class="hero">
  <div class="photo" role="img" aria-label="Two-storey luxury home with tiled roof, green lawn and blue sky"></div>
  <div class="hero-shade"></div>
  <div class="abs hero-kicker">Trueline Homes</div>
  <h1 class="abs display hero-title">Building More<br>Than Dream<br>Luxury Homes</h1>
  <a class="btn hero-btn">Learn More &nbsp;›</a>
  <svg class="hero-arrow" style="left:50px" width="20" height="30" viewBox="0 0 20 30"><path d="M15 3 4 15l11 12" fill="none" stroke="#fff" stroke-width="3"/></svg>
  <svg class="hero-arrow" style="left:1119px" width="20" height="30" viewBox="0 0 20 30"><path d="m5 3 11 12L5 27" fill="none" stroke="#fff" stroke-width="3"/></svg>
</section>

<section class="about">
  <svg class="abs" style="left:0;top:0" width="1200" height="554">
    <defs>
      <linearGradient id="aboutPhoto" x1="0" y1="0" x2="0" y2="1">
        <stop offset="0" stop-color="#8fb4cf"/><stop offset=".5" stop-color="#c9b59c"/><stop offset=".8" stop-color="#5c6a63"/><stop offset="1" stop-color="#2d6f96"/>
      </linearGradient>
      <filter id="cardShadow" x="-10%" y="-10%" width="120%" height="130%"><feDropShadow dx="0" dy="8" stdDeviation="14" flood-color="#1b3a5a" flood-opacity=".12"/></filter>
    </defs>
    <polygon points="0,0 772,0 489,554 0,554" fill="url(#aboutPhoto)" role="img" aria-label="Modern white and timber villa with glass balconies beside a pool at dusk"/>
    <polygon points="772,101 1075,101 927,466 466,466 623,101" fill="#fff" filter="url(#cardShadow)"/>
    <polyline points="772,463 1001,463 1075,314" fill="none" stroke="#12ab8a" stroke-width="8"/>
  </svg>
  <h2 class="abs display about-title">About<br>Trueline Homes</h2>
  <div class="rule" style="left:637px;top:225px;width:28px"></div>
  <p>Lorem ipsum dolor sit amet, consectetur adipiscing elit, sed do eiusmod tempor incididunt ut labore et dolore magna aliqua. Ut enim ad minim veniam, quis nostrud exercitation ullamco laboris lorem ipsum dolor sit amet, consectetur adipiscing elit, sed do eiusmod tempor incidid</p>
  <a class="btn about-btn">Learn More</a>
</section>

<section class="featured">
  <h2 class="display section-title">Featured Homes</h2>
  <svg class="abs" style="left:519px;top:102px" width="162" height="5"><rect y="1.5" width="162" height="1" fill="#8cc6ea"/><rect x="61" y="0" width="40" height="4" fill="#1b8fd6"/></svg>
  <div class="photo card-img" style="left:111px;background:linear-gradient(160deg,#d9e2ea,#9aa8b4 60%,#3c4650)" role="img" aria-label="Luxury dining room with chandelier and city view windows"></div>
  <div class="photo card-img" style="left:447px;background:linear-gradient(160deg,#eceae6,#b9a58a 55%,#4f4a44)" role="img" aria-label="Open living room with timber staircase and sofa"></div>
  <div class="photo card-img" style="left:782px;background:linear-gradient(180deg,#bcdcf5,#e9eef2 50%,#7c8c86)" role="img" aria-label="White multi-storey residence with balconies under a blue sky"></div>
  <div class="card-text card-light" style="left:126px;top:366px;width:282px;height:81px"><h3>Luxury Home</h3>Lorem ipsum dolor sit amet, consectetur adipiscing elit, sed do eiusmod</div>
  <div class="card-text card-blue" style="left:458px;top:346px;width:282px;height:106px;padding-top:34px"><h3>Luxury Home</h3>Lorem ipsum dolor sit amet, consectetur adipiscing elit, sed do eiusmod</div>
  <div class="card-text card-light" style="left:797px;top:351px;width:281px;height:106px;padding-top:34px"><h3>Luxury Home</h3>Lorem ipsum dolor sit amet, consectetur adipiscing elit, sed do eiusmod</div>
</section>

<section class="services">
  <div class="photo" role="img" aria-label="Blue-tinted modern interior with tall windows"></div>
  <div class="services-kicker">WHAT WE DO</div>
  <h2 class="display section-title">Services Provide</h2>
  <svg class="abs" style="left:0;top:0" width="1200" height="564">
    <g fill="#3ba3e4">
      <polygon points="136,311 308,139 300,131 116,311 300,491 308,483"/>
      <polygon points="721,311 893,139 885,131 701,311 885,491 893,483"/>
      <polygon points="1065,311 893,139 901,131 1085,311 901,491 893,483"/>
    </g>
    <polygon points="598,121 788,311 598,501 408,311" fill="none" stroke="#8cc8f0" stroke-width="1.5"/>
    <polygon points="308,139 480,311 308,483 136,311" fill="#fff"/>
    <polygon points="598,139 770,311 598,483 426,311" fill="#12ab8a"/>
    <polygon points="893,139 1065,311 893,483 721,311" fill="#fff"/>
    <g fill="none" stroke-width="2" stroke-linecap="round" stroke-linejoin="round">
      <path d="m288 260v-40h40v40zm8-8 8-10 6 6 10-12" stroke="#1b8fd6"/>
      <path d="m598 218v8m-6 34 6-34 6 34m-10-12h8" stroke="#fff"/>
      <circle cx="598" cy="230" r="4" stroke="#fff"/>
      <path d="m873 222h36v38h-36zm0 12h36m-24 0v26" stroke="#1b8fd6"/>
    </g>
    <g fill="none" stroke-width="2.5">
      <path d="m300 407 8 8 8-8" stroke="#1b8fd6"/>
      <path d="m590 404 8 8 8-8" stroke="#fff"/>
      <path d="m885 400 8 8 8-8" stroke="#1b8fd6"/>
    </g>
  </svg>
  <div class="service service-light" style="left:208px;top:284px"><h3>Design &amp;<br>Build</h3><p>Lorem ipsum dolor sit amet<br>consectetur adipiscing elit sed<br>do eiusmodsum dolor sit</p></div>
  <div class="service service-green" style="left:498px;top:284px"><h3>Architects</h3><p>Lorem ipsum dolor sit amet<br>consectetur adipiscing elit sed<br>do eiusmodsum dolor sit</p></div>
  <div class="service service-light" style="left:793px;top:284px"><h3>Interiors</h3><p>Lorem ipsum dolor sit amet<br>consectetur adipiscing elit sed<br>do eiusmodsum dolor</p></div>
</section>

<section class="why">
  <svg class="abs" style="left:0;top:0" width="1200" height="622">
    <defs>
      <linearGradient id="whyTop" x1="0" y1="0" x2="1" y2="0"><stop offset="0" stop-color="#dbe6ee"/><stop offset=".6" stop-color="#b7c6d0"/><stop offset="1" stop-color="#6f9c5c"/></linearGradient>
      <linearGradient id="whyBottom" x1="0" y1="0" x2="0" y2="1"><stop offset="0" stop-color="#dfe7ee"/><stop offset=".5" stop-color="#8a7c70"/><stop offset="1" stop-color="#5a6b4e"/></linearGradient>
    </defs>
    <polygon points="505,420 993,420 1053,279 1017,280 960,410" fill="#1b8fd6"/>
    <polygon points="536,74 1163,74 994,504 505,504" fill="#12ab8a"/>
    <polygon points="128,109 536,109 492,263 83,263" fill="url(#whyTop)" role="img" aria-label="Architect's hand with pen beside a small model house on plans"/>
    <polyline points="492,206 546,206 521,280" fill="none" stroke="#a9cfe8" stroke-width="3"/>
    <polygon points="208,271 610,271 560,524 156,524" fill="url(#whyBottom)" role="img" aria-label="Two-storey contemporary family home with balcony"/>
    <polyline points="128,362 96,451 208,451" fill="none" stroke="#a9cfe8" stroke-width="3"/>
  </svg>
  <h2 class="abs display why-title">Why Choose<br>Trueline Homes</h2>
  <div class="rule" style="left:647px;top:229px;width:26px;background:#fff"></div>
  <p>Lorem ipsum dolor sit amet, consectetur adipiscing elit, sed do eiusmod tempor incididunt ut labore et dolore magna aliqua. Ut enim ad minim veniam, quis nostrud exercitation ullamco laboris lorem ipsum dolor sit amet, consectetur adipiscing elit, sed do eiusmod tempor incidid</p>
  <a class="btn why-btn">Learn More</a>
</section>

<section class="how">
  <svg class="abs" style="left:0;top:0" width="1200" height="546">
    <defs>
      <linearGradient id="howPhoto" x1="0" y1="0" x2="1" y2="1"><stop offset="0" stop-color="#e7ece9"/><stop offset=".45" stop-color="#b9c2bf"/><stop offset=".75" stop-color="#5e7368"/><stop offset="1" stop-color="#d8dcdc"/></linearGradient>
    </defs>
    <polygon points="721,0 1200,0 1200,546 477,546" fill="url(#howPhoto)" role="img" aria-label="Two architects reviewing plans and a tablet at a desk"/>
  </svg>
  <h2 class="abs display how-title">How We Build<br>Your Luxury Home</h2>
  <p>Lorem ipsum dolor sit amet, consectetur adipiscing elit, sed do eiusmod tempor incididunt ut labore et dolore magna aliqua. Ut enim ad minim veniam, quis nostrud exercitation ullamco laboris lorem ipsum dolor sit amet, consectetur adipiscing elit, sed do eiusmod tempor incidid</p>
  <a class="btn how-btn">Learn More</a>
</section>

<section class="start">
  <div class="start-frame"></div>
  <div class="start-accent"></div>
  <div class="photo start-img" style="background:linear-gradient(160deg,#5d7f9e,#3a4a5c 45%,#8a5a36 70%,#2b2a2a)" role="img" aria-label="Modern dark-clad house with warm lit windows at twilight"></div>
  <h2 class="abs display start-title">Start Building<br>Your Project</h2>
  <p>Lorem ipsum dolor sit amet, consectetur adipiscing elit, sed do eiusmod tempor incididunt ut labore et dolore magna aliqua.</p>
  <a class="btn start-btn">Get Start Your Project</a>
</section>

<footer class="site-footer">
  <div class="footer-mark"></div>
  <div class="footer-brand">Trueline Homes</div>
  <div class="footer-divider"></div>
  <div class="footer-rule"></div>
  <span class="footer-nav" style="left:371px">About Us</span>
  <span class="footer-nav" style="left:495px">Services</span>
  <span class="footer-nav" style="left:617px">Projects</span>
  <span class="footer-nav" style="left:741px">Why Us</span>
  <span class="footer-nav" style="left:853px">Blogs</span>
  <span class="footer-nav" style="left:954px">Contact Us</span>
  <div class="copyright">Copyright © 2023 Trueline Homes. All rights reserved.</div>
  <span class="social" style="left:940px"></span>
  <span class="social" style="left:977px"></span>
  <span class="social" style="left:1012px"></span>
</footer>

</body>
</html>
```